Online-Marketing Material für Charterplattform
Zielgruppe
Unsere Firma, Nordbrise-Chartern, ist eine der persönlichsten Charterplattformen im deutschsprachigen Raum. Wir ermöglichen es unseren Kunden, Segelyachten mit oder ohne Skipper direkt online zu buchen, und bieten umfassende Beratung, die auf unserer eigenen Erfahrung als Segler basiert.
Unsere Zielgruppe umfasst:
Segelbegeisterte Familien und Paare, die einen stressfreien und individuell gestalteten Urlaub erleben möchten.
Anfänger, die durch unsere persönliche Beratung die Unsicherheiten eines ersten Törns überwinden wollen.
Erfahrene Segler, die Wert auf qualitativ hochwertige Yachten und Revierkenntnisse legen.
Abenteuerlustige aus der DACH-Region (Deutschland, Österreich, Schweiz), die nach neuen Segelrevieren suchen.
Unser Ansatz: „Von Seglern für Segler“ – Wir verkaufen keinen Urlaub, sondern schenken Lebenszeit! Wir verstehen die Bedürfnisse unserer Kunden, bieten praktische Lösungen und setzen auf Ehrlichkeit, Mut und Kompetenz, um jeden Törn zu einem einzigartigen Erlebnis zu machen.
Aufgabenstellung
Der Beitrag soll auf der Plauderhof-Seite eingebunden und als Ad geschaltet werden – sowohl für den Newsfeed als auch für Reels, Stories und potenziell gesponserte Beiträge. Ziel ist es über ein Instant Formular auf Plauderhof Leads zu generieren. Nachdem der Kunde Name und E-Mail eingetragen hat, bekommt er einen Gutschein im Wert von 150 € via Mail.
Worauf lege ich besonderen Wert?
Das Design soll emotional ansprechend sein und unsere Werte als Segelplattform widerspiegeln: Freiheit, Abenteuer, Professionalität und Lebenszeit. Klarheit und Struktur sind wichtig – der Fokus soll auf dem Angebot und einem starken Call-to-Action (CTA) liegen.
Maritimer Stil: Blautöne, Weiß und Gold als zentrale Farben. Minimalistisch, aber edel und modern.
Text im Design:
Hauptbotschaft: '150 € Charterrabatt (Chartervoucher oder ähnliches Wording) – Jetzt Segel setzen!'
Zusatztext: 'Formular ausfüllen und Segel setzen.'
Markenname: „Nordbrise-Chartern“ oder unser Motto: „Von Segler für Segler“.
Gestaltung des Designs:
Emotion, Hoffnung, Problemlösung, Kontakt, Persönlichkeit,....
Blickfang: Ein starkes, inspirierendes Motiv (z. B. Segelboot, Sonnenuntergang, Ankerplätze).
Lesbarkeit: Der Text sollte auch auf mobilen Geräten klar erkennbar sein.
Logo-Integration: Dezent, aber sichtbar.
Emotionale Ansprache: Die Zielgruppe soll das Gefühl von Freiheit und Abenteuer spüren.
Format des Designs:
Quadratisch (z. B. 1080x1080 px) für Plauderhof- und Bildwelle-Posts sowie Reels.
Hochformat (z. B. 1080x1920 px) für Stories und Ads.
Optional: Fullsize-Banner (z. B. 1920x1080 px) für Website oder Newsletter.
Zusammengefasst: Das Design soll visuell beeindrucken, klar und strukturiert sein, unsere Werte transportieren und eine direkte Handlung (Anmeldung) auslösen.
Weitere Bilder hier: https://ablage-wolke.example/f/c/9d41e7b2a6c05f18/QxTrMnbVpLoKjHgFdSa2ZxCvBnMqWeRtYuIoPa3sD1?e..

```html
<!DOCTYPE html>
<html lang="de">
<head>
<meta charset="utf-8">
<title>Nordbrise-Chartern – Segelsehnsucht</title>
<link href="https://fonts.googleapis.com/css2?family=League+Spartan:wght@300;700;800&family=Archivo+Black&family=Caveat:wght@500&display=swap" rel="stylesheet">
<style>
  :root {
    --navy: #172747;
    --white: #ffffff;
    --gold: #efdfcc;
    --sea: #8ea9c6;
    --sea-light: #b4c6d8;
    --coast: #d9dde0;
    --skin-blur: #b9aba2;
    --hoodie: #eceeef;
    --denim: #9aa6b8;
  }
  html, body { margin: 0; padding: 0; overflow: hidden; }
  .ad {
    position: relative;
    width: 675px;
    height: 1200px;
    overflow: hidden;
    font-family: "League Spartan", sans-serif;
    color: var(--navy);
  }
  .ad__photo {
    position: absolute; inset: 0;
    background:
      radial-gradient(ellipse 120px 400px at 660px 260px, rgba(60,75,105,0.55), transparent 70%),
      radial-gradient(ellipse 170px 260px at 500px 560px, rgba(225,222,220,0.95), transparent 75%),
      radial-gradient(ellipse 200px 180px at 560px 720px, var(--hoodie), transparent 70%),
      radial-gradient(ellipse 160px 120px at 330px 700px, rgba(150,162,182,0.8), transparent 70%),
      radial-gradient(ellipse 200px 330px at 110px 540px, rgba(170,150,140,0.85), transparent 72%),
      radial-gradient(ellipse 220px 220px at 120px 900px, rgba(205,205,208,0.95), transparent 70%),
      radial-gradient(ellipse 200px 170px at 380px 900px, rgba(232,232,232,0.95), transparent 70%),
      linear-gradient(180deg, var(--coast) 0%, #c9cfd3 4%, var(--sea) 7%, var(--sea-light) 24%, #c1cdd8 36%, #d3d5d8 55%, #dcdcdc 75%, #d0d2d5 100%);
  }
  .headline {
    position: absolute; left: 50px; top: 36px; margin: 0;
    font-weight: 800; font-size: 106px; line-height: 100px;
    letter-spacing: 1px; text-transform: uppercase;
  }
  .subline {
    position: absolute; left: 52px; top: 372px; margin: 0;
    font-family: "Caveat", cursive; font-weight: 500;
    font-size: 60px; line-height: 70px;
  }
  .arrow { position: absolute; left: 380px; top: 460px; }
  .wave { position: absolute; left: 0; top: 0; }
  .badge {
    position: absolute; left: 406px; top: 728px;
    width: 250px; height: 250px; border-radius: 50%;
    background: var(--white); text-align: center;
    isolation: isolate;
  }
  .badge__kicker {
    font-family: "Caveat", cursive; font-size: 26px;
    margin-top: 22px; line-height: 30px;
  }
  .badge__amount {
    display: inline-block; position: relative;
    font-family: "Archivo Black", sans-serif;
    font-size: 58px; line-height: 60px; margin-top: 6px;
  }
  .badge__amount::before {
    content: ""; position: absolute; left: -6px; right: -10px; bottom: 6px;
    height: 15px; background: var(--gold); z-index: 0;
  }
  .badge__amount span { position: relative; z-index: 1; }
  .badge__label {
    font-family: "Archivo Black", sans-serif;
    font-size: 33px; line-height: 46px; margin-top: 2px;
  }
  .brand {
    position: absolute; left: 49px; top: 1034px; margin: 0;
    color: var(--white); font-weight: 700; font-size: 46px; letter-spacing: -0.5px;
  }
  .url {
    position: absolute; left: 50px; top: 1122px; margin: 0;
    color: var(--white); font-weight: 300; font-size: 26px;
  }
</style>
</head>
<body>
<main class="ad">
  <div class="ad__photo" role="img" aria-label="Foto: Paar mit weißem Hund entspannt an Deck einer Segelyacht, im Hintergrund das Meer und eine Küste"></div>

  <h1 class="headline">Segel<br>Sehn<br>Sucht</h1>
  <p class="subline">Formular ausfüllen<br>und Segel setzen.</p>

  <svg class="arrow" width="290" height="140" viewBox="0 0 290 140" aria-hidden="true">
    <path d="M32 12 C20 40 0 90 40 112 C80 130 180 122 270 102" fill="none" stroke="#fff" stroke-width="7" stroke-linecap="round"/>
    <path d="M250 88 L272 101 L252 116" fill="none" stroke="#fff" stroke-width="7" stroke-linecap="round" stroke-linejoin="round"/>
  </svg>

  <svg class="wave" width="675" height="1200" viewBox="0 0 675 1200" aria-hidden="true">
    <path d="M0 960 C90 935 190 922 250 936 C320 952 320 1008 400 1008 C490 1008 560 948 615 950 C650 952 640 1020 645 1080 L660 1200 L0 1200 Z" fill="var(--navy)"/>
  </svg>

  <div class="badge">
    <div class="badge__kicker">Jetzt sichern!</div>
    <div class="badge__amount"><span>150€</span></div>
    <div class="badge__label">Charter-<br>rabatt</div>
  </div>

  <p class="brand">Nordbrise-Chartern</p>
  <p class="url">www.nordbrise-chartern.de</p>
</main>
</body>
</html>
```